Need a Brochure Design

We need a brochure designed (A4 two sides or A3 foldable which is equal to 2 x A4 = total of four pages )

Brief and Logo attached.

```html
<!DOCTYPE html>
<html lang="en">
<head>
<meta charset="utf-8">
<title>Nest Staging Co. – Brochure</title>
<link href="https://fonts.googleapis.com/css2?family=Montserrat:wght@400;500;600&family=Open+Sans:wght@400;600&family=Dancing+Script:wght@500&display=swap" rel="stylesheet">
<style>
:root{
  --backdrop:#d4d3d2;
  --paper:#ffffff;
  --paper-warm:#ece9e7;
  --peach:#f3d3bf;
  --peach-soft:#f8e6da;
  --salmon:#e0a27f;
  --ink:#6b6b6b;
  --ink-dark:#4f4f4f;
  --band:#a3a3a3;
  --cell:#b7b7b9;
  --cell-dark:#9d9da0;
}
*{box-sizing:border-box;margin:0;padding:0}
html,body{width:798px;height:1200px;overflow:hidden;background:var(--backdrop)}
body{position:relative;font-family:"Open Sans",Arial,sans-serif;color:var(--ink)}
.spread{position:absolute;left:19px;width:760px;height:537px;display:flex;box-shadow:0 4px 14px rgba(0,0,0,.18)}
.spread--outer{top:30px}
.spread--inner{top:633px}
.page{position:relative;width:380px;height:537px;overflow:hidden;background:var(--paper)}
.page--warm{background:var(--paper-warm)}
.photo{position:absolute}
.body-text{font-size:7px;line-height:1.55;color:var(--ink)}
.heading{font-family:"Montserrat",Arial,sans-serif;font-weight:500;letter-spacing:.06em;text-transform:uppercase;color:var(--ink-dark)}
.accent{font-family:"Montserrat",Arial,sans-serif;font-weight:600;font-size:7.5px;letter-spacing:.08em;text-transform:uppercase;color:var(--salmon)}
.brand-name{font-family:"Montserrat",Arial,sans-serif;font-weight:500;font-size:9px;letter-spacing:.14em;text-transform:uppercase;color:var(--ink-dark);display:flex;align-items:center;gap:5px}
.brand-name .dot{width:6px;height:6px;border-radius:50%;background:var(--salmon)}

/* intro page */
.intro__swirl{position:absolute;inset:0}
.intro__portrait-blob{position:absolute;left:168px;top:42px;width:120px;height:120px;border-radius:50%;background:var(--peach)}
.intro__portrait{left:128px;top:42px;width:116px;height:116px;border-radius:50%;background:radial-gradient(circle at 50% 40%,#d9d4d2,#a9a5a6 70%,#8e8a8c)}
.intro__content{position:absolute;left:40px;top:180px;width:300px}
.intro__content p{margin-bottom:8px}
.intro__hello{font-size:8px;margin-bottom:6px}
.intro__script{font-family:"Dancing Script",cursive;font-size:17px;color:var(--salmon);margin:10px 0 6px}
.intro__ps{margin-top:14px}
.contact-band{position:absolute;left:0;bottom:0;width:100%;height:30px;background:var(--band);display:flex;justify-content:space-around;align-items:center;font-size:7px;color:#fff}
.contact-band span{display:flex;align-items:center;gap:4px}

/* cover */
.cover__logo-blob{position:absolute;left:40px;top:18px;width:90px;height:80px;border-radius:48% 52% 40% 60%;background:var(--peach)}
.cover__logo{position:absolute;left:28px;top:48px}
.cover__photo{left:0;top:96px;width:380px;height:330px;background:linear-gradient(160deg,#efeeec 0%,#d8d6d4 35%,#bdb8b2 60%,#a48a6a 85%,#7d6650 100%)}
.cover__curve{position:absolute;left:0;bottom:0}
.cover__tagline{position:absolute;right:34px;bottom:58px;text-align:right;font-size:17px;line-height:1.2;letter-spacing:.08em}
.cover__web{position:absolute;right:34px;bottom:34px;font-size:9px;color:var(--salmon);display:flex;align-items:center;gap:5px}

/* connected page */
.connected__photo{left:0;top:0;width:380px;height:215px;background:linear-gradient(170deg,#f3f3f2 0%,#dadcd9 40%,#8f9a88 60%,#b98a5e 85%,#9c6e45 100%)}
.connected__blob{position:absolute;left:-30px;top:200px;width:190px;height:170px;border-radius:55% 45% 50% 50%;background:var(--peach)}
.connected__title{position:absolute;left:32px;top:268px;font-size:13px;line-height:1.3}
.connected__text{position:absolute;left:172px;top:228px;width:180px}
.connected__text ul{list-style:none;margin:4px 0 8px}
.connected__text li::before{content:"•";color:var(--salmon);margin-right:4px}
.voucher{display:flex;align-items:center;gap:8px;border:1px solid #c9c6c4;border-radius:4px;padding:5px 8px;margin:6px 0 10px}
.voucher__amount{font-family:"Montserrat",Arial,sans-serif;font-size:18px;color:var(--ink-dark)}
.voucher__text{font-size:6.5px;line-height:1.4}
.connected__wave{position:absolute;left:0;bottom:0}

/* packages page */
.collage{position:absolute;left:0;top:0;width:380px;height:190px;display:grid;grid-template-columns:1fr 1fr;grid-template-rows:1fr 1fr;gap:3px;background:#fff}
.collage .photo{position:static}
.collage__a{background:linear-gradient(135deg,#cfcac6,#8d8884)}
.collage__b{background:linear-gradient(135deg,#e7e5e6,#9a9a9c)}
.collage__c{background:linear-gradient(135deg,#d7dde2,#a7b3bf)}
.collage__d{background:linear-gradient(135deg,#ece9ea,#8e8c99)}
.packages{position:absolute;left:28px;top:210px;width:330px}
.packages__title{font-size:14px;margin-bottom:4px}
.price-table{width:100%;border-collapse:separate;border-spacing:0 2px;margin:6px 0 12px;font-size:6.5px;color:#fff}
.price-table td{background:var(--cell);padding:4px 6px}
.price-table td:last-child{background:var(--cell-dark);text-align:right;white-space:nowrap}
.packages ul{list-style:none;width:220px}
.packages li{margin-bottom:2px}
.packages li::before{content:"•";color:var(--salmon);margin-right:4px}
.packages__logo-blob{position:absolute;right:28px;top:370px;width:70px;height:60px;border-radius:50%;background:var(--peach-soft)}
.packages__logo{position:absolute;right:24px;top:392px}
</style>
</head>
<body>

<section class="spread spread--outer">
  <article class="page page--warm intro">
    <svg class="intro__swirl" width="380" height="537" viewBox="0 0 380 537" aria-hidden="true">
      <path d="M60 537 C 40 380, 120 300, 230 250 C 330 205, 360 120, 380 60 L380 537 Z" fill="#f4f2f0"/>
    </svg>
    <div class="intro__portrait-blob"></div>
    <div class="photo intro__portrait" role="img" aria-label="Portrait of the founder"></div>
    <div class="intro__content body-text">
      <p class="intro__hello heading">Hey there,</p>
      <p>I'm Mara Ellis, founder and creative director of Nest Staging Co. Below is a short introduction to who we are and what we do.</p>
      <p>We have styled homes across the city since 2016, helping owners and agents present every room at its best and sell with confidence.</p>
      <p class="intro__script">Because first impressions count.</p>
      <p>A great first look brings more buyers through the door. At Nest Staging Co. we plan each room, bring the furniture, and handle every detail so your home feels warm, bright and ready to sell.</p>
      <p>Our styling includes a free consultation, large storage space and quick delivery.</p>
      <p class="accent intro__ps">P.S. Let's contact us</p>
    </div>
    <div class="contact-band">
      <span>✉ hello@neststagingco.com.au</span>
      <span>
        <svg width="8" height="8" viewBox="0 0 24 24" aria-hidden="true"><path fill="#fff" d="M6.6 10.8a15 15 0 006.6 6.6l2.2-2.2a1 1 0 011-.25 11.4 11.4 0 003.6.6 1 1 0 011 1V20a1 1 0 01-1 1A17 17 0 013 4a1 1 0 011-1h3.5a1 1 0 011 1c0 1.25.2 2.45.6 3.6a1 1 0 01-.25 1z"/></svg>
        0400 123 456</span>
      <span>neststagingco.com.au</span>
    </div>
  </article>

  <article class="page cover">
    <div class="cover__logo-blob"></div>
    <div class="cover__logo brand-name"><span class="dot"></span>Nest Staging Co.</div>
    <div class="photo cover__photo" role="img" aria-label="Staged living room with sofa, round coffee tables and a garden window"></div>
    <svg class="cover__curve" width="380" height="150" viewBox="0 0 380 150" aria-hidden="true">
      <path d="M0 40 C 120 -10, 260 0, 380 30 L380 150 L0 150 Z" fill="#f1efed"/>
      <path d="M0 52 C 130 5, 260 12, 380 42" fill="none" stroke="#e7c9b6" stroke-width="1"/>
    </svg>
    <p class="cover__tagline heading">We will give<br>your property the<br>best look!</p>
    <p class="cover__web">
      <svg width="9" height="9" viewBox="0 0 10 10" aria-hidden="true"><circle cx="5" cy="5" r="4" fill="none" stroke="currentColor"/><path d="M1 5h8M5 1c2 2.5 2 5.5 0 8M5 1c-2 2.5-2 5.5 0 8" fill="none" stroke="currentColor" stroke-width=".7"/></svg>
      neststagingco.com.au</p>
  </article>
</section>

<section class="spread spread--inner">
  <article class="page page--warm connected">
    <div class="photo connected__photo" role="img" aria-label="Open plan dining and living area with timber floor"></div>
    <div class="connected__blob"></div>
    <p class="connected__title heading">We're well<br>connected</p>
    <div class="connected__text body-text">
      <p>We have a steady flow of clients who have not yet secured their real estate agent, so we're happy to share the love. We believe in partnerships and we work with reputable agents across the city.</p>
      <p class="accent" style="margin-top:8px">Why choose Nest Staging Co.?</p>
      <ul>
        <li>Experienced, enthusiastic property stylists</li>
        <li>Work with low client budgets</li>
        <li>Fast turnaround in a tight timeline</li>
        <li>Flexible rental terms (4/6/8 weeks)</li>
        <li>Ready to recommend potential customers</li>
      </ul>
      <p class="accent">We reward referrals!</p>
      <div class="voucher">
        <span class="voucher__amount">$200</span>
        <span class="voucher__text">We offer a $200 gift voucher for every successful referral to us!</span>
      </div>
      <p>We'd love to hear from you, so please contact us by telephone, text, or email on 0400 123 456 or hello@neststagingco.com.au</p>
      <p style="margin-top:6px">Please visit our website: neststagingco.com.au</p>
    </div>
    <svg class="connected__wave" width="380" height="60" viewBox="0 0 380 60" aria-hidden="true">
      <path d="M0 60 L0 30 C 90 10, 180 50, 280 25 C 330 12, 360 20, 380 28 L380 60 Z" fill="#f4f2f0"/>
    </svg>
  </article>

  <article class="page packages-page">
    <div class="collage">
      <div class="photo collage__a" role="img" aria-label="Hands arranging a decorative object"></div>
      <div class="photo collage__b" role="img" aria-label="The styling team standing together"></div>
      <div class="photo collage__c" role="img" aria-label="Stylists making up a bed"></div>
      <div class="photo collage__d" role="img" aria-label="Styled bed with patterned cushions"></div>
    </div>
    <div class="packages body-text">
      <h2 class="packages__title heading">Nest Staging Co.</h2>
      <p>We average over 100 property styling projects per year, with a large proportion selling in less than 30 days</p>
      <p class="accent" style="margin-top:6px">Our package price</p>
      <table class="price-table">
        <tr><td>1 Bedroom Property</td><td>Full styling, 4 weeks, free storage</td><td>$1,800.00 AUD</td></tr>
        <tr><td>2 Bedroom Property</td><td>Full styling, 4 weeks, free storage</td><td>$2,600.00 AUD</td></tr>
        <tr><td>3 Bedroom Property</td><td>Full styling, 4 weeks, free storage</td><td>$3,000.00 AUD</td></tr>
        <tr><td>4 Bedroom Property</td><td>Full styling, 4 weeks, free storage</td><td>$3,800.00 AUD</td></tr>
      </table>
      <ul>
        <li>Helping your property reach its highest potential without busting the budget.</li>
        <li>Achieving a record number of viewings and the highest possible sale price.</li>
        <li>Inspiration, interior design and decoration, and removal included.</li>
        <li>Pre-sale home preparation by available services.</li>
        <li>Free consultation and longer rental periods.</li>
        <li>A small investment for such a large transformation.</li>
      </ul>
    </div>
    <div class="packages__logo-blob"></div>
    <div class="packages__logo brand-name"><span class="dot"></span>Nest Staging Co.</div>
  </article>
</section>

</body>
</html>
```